Packaging designed for both the bar and the box for retail and online sales

The name of the product is Plume Crumb. We manufacture a consumer package good product that's a healthy edible cookie dough bar. The product look, feels and tastes like cookie dough. It's sold in the refrigerator section of retail stores next to cookie dough and tundra loaf. The product is Gluten Free, Diary Free and include B-12, Biotin and Collagen. The ingredients are natural. When design this think about who eat cookie dough and how to engage the buyer in purchasing the product.

We needs design packaging designed for both the bar and the box. I have attached the die lines for both products.

Target Market(s)

Our customer is 16-45. Primarily female but really anyone. Middle to upper income. Interest include healthy life style and yoga. Like to eat something sweet but not feel guilty.

Colors

Designer to choose colors to be used in the design.

Requirements
Must have
• Must be clean, warm, inviting. Brand designs I really like are Tundra Loaf.
Should not have
• Should not have a photo of food

```html
<!DOCTYPE html>
<html lang="en">
<head>
<meta charset="utf-8">
<title>Plume Crumb – bar wrappers</title>
<link rel="stylesheet" href="https://fonts.googleapis.com/css2?family=Quicksand:wght@500;700&display=swap">
<style>
  :root {
    --bg-top: #f1f1f3;
    --bg-bottom: #dcdce0;
    --white: #ffffff;
    --ink: #3a2a22;
    --mustard: #e5b534;
    --violet: #8a4fc6;
    --sky: #5b8fc9;
  }
  html, body {
    margin: 0;
    padding: 0;
    width: 1200px;
    height: 756px;
    overflow: hidden;
  }
  .canvas {
    position: relative;
    width: 1200px;
    height: 756px;
    background: linear-gradient(180deg, var(--bg-top), var(--bg-bottom));
  }
  .wrapper {
    position: absolute;
    left: 100px;
    width: 1000px;
    height: 180px;
    display: block;
  }
  .wrapper--honey  { top: 60px;  --tone: var(--mustard); }
  .wrapper--violet { top: 288px; --tone: var(--violet); }
  .wrapper--sky    { top: 516px; --tone: var(--sky); }

  .tone      { fill: var(--tone); }
  .crimp     { fill: var(--tone); opacity: .85; }
  .panel     { fill: var(--white); }
  .ring      { fill: none; stroke: var(--tone); stroke-width: 5; }
  .dot       { fill: var(--tone); }
  .badge     { fill: none; stroke: var(--white); stroke-width: 3; }
  .brand-name {
    font-family: "Quicksand", sans-serif;
    font-weight: 700;
    font-size: 52px;
    fill: var(--ink);
  }
  .benefits {
    font-family: "Quicksand", sans-serif;
    font-weight: 500;
    font-size: 24px;
    fill: var(--white);
  }
</style>
</head>
<body>
<main class="canvas">

  <svg class="wrapper wrapper--honey" viewBox="0 0 1000 180" aria-label="Plume Crumb bar wrapper, honey">
    <path class="crimp" d="M24 0 L0 0 L8 10 L0 20 L8 30 L0 40 L8 50 L0 60 L8 70 L0 80 L8 90 L0 100 L8 110 L0 120 L8 130 L0 140 L8 150 L0 160 L8 170 L0 180 L24 180Z"/>
    <path class="crimp" d="M976 0 L1000 0 L992 10 L1000 20 L992 30 L1000 40 L992 50 L1000 60 L992 70 L1000 80 L992 90 L1000 100 L992 110 L1000 120 L992 130 L1000 140 L992 150 L1000 160 L992 170 L1000 180 L976 180Z"/>
    <rect class="tone" x="22" y="0" width="956" height="180"/>
    <polygon class="panel" points="270,0 770,0 650,180 150,180"/>
    <rect class="badge" x="50" y="22" width="56" height="56" rx="8"/>
    <rect class="badge" x="50" y="100" width="56" height="56" rx="8"/>
    <circle class="ring" cx="310" cy="24" r="10"/>
    <circle class="dot" cx="380" cy="20" r="8"/>
    <circle class="ring" cx="460" cy="22" r="12"/>
    <circle class="ring" cx="610" cy="30" r="22"/>
    <circle class="dot" cx="640" cy="80" r="9"/>
    <circle class="ring" cx="560" cy="156" r="14"/>
    <circle class="dot" cx="615" cy="158" r="7"/>
    <circle class="ring" cx="200" cy="160" r="10"/>
    <text class="brand-name" x="240" y="112">Plume Crumb</text>
    <text class="benefits" x="745" y="70">+vitamin B12</text>
    <text class="benefits" x="760" y="100">biotin</text>
    <text class="benefits" x="760" y="130">collagen</text>
  </svg>

  <svg class="wrapper wrapper--violet" viewBox="0 0 1000 180" aria-label="Plume Crumb bar wrapper, violet">
    <path class="crimp" d="M24 0 L0 0 L8 10 L0 20 L8 30 L0 40 L8 50 L0 60 L8 70 L0 80 L8 90 L0 100 L8 110 L0 120 L8 130 L0 140 L8 150 L0 160 L8 170 L0 180 L24 180Z"/>
    <path class="crimp" d="M976 0 L1000 0 L992 10 L1000 20 L992 30 L1000 40 L992 50 L1000 60 L992 70 L1000 80 L992 90 L1000 100 L992 110 L1000 120 L992 130 L1000 140 L992 150 L1000 160 L992 170 L1000 180 L976 180Z"/>
    <rect class="tone" x="22" y="0" width="956" height="180"/>
    <polygon class="panel" points="270,0 770,0 650,180 150,180"/>
    <rect class="badge" x="50" y="22" width="56" height="56" rx="8"/>
    <rect class="badge" x="50" y="100" width="56" height="56" rx="8"/>
    <circle class="ring" cx="310" cy="24" r="10"/>
    <circle class="dot" cx="380" cy="20" r="8"/>
    <circle class="ring" cx="460" cy="22" r="12"/>
    <circle class="ring" cx="610" cy="30" r="22"/>
    <circle class="dot" cx="640" cy="80" r="9"/>
    <circle class="ring" cx="560" cy="156" r="14"/>
    <circle class="dot" cx="615" cy="158" r="7"/>
    <circle class="ring" cx="200" cy="160" r="10"/>
    <text class="brand-name" x="240" y="112">Plume Crumb</text>
    <text class="benefits" x="745" y="70">+vitamin B12</text>
    <text class="benefits" x="760" y="100">biotin</text>
    <text class="benefits" x="760" y="130">collagen</text>
  </svg>

  <svg class="wrapper wrapper--sky" viewBox="0 0 1000 180" aria-label="Plume Crumb bar wrapper, sky blue">
    <path class="crimp" d="M24 0 L0 0 L8 10 L0 20 L8 30 L0 40 L8 50 L0 60 L8 70 L0 80 L8 90 L0 100 L8 110 L0 120 L8 130 L0 140 L8 150 L0 160 L8 170 L0 180 L24 180Z"/>
    <path class="crimp" d="M976 0 L1000 0 L992 10 L1000 20 L992 30 L1000 40 L992 50 L1000 60 L992 70 L1000 80 L992 90 L1000 100 L992 110 L1000 120 L992 130 L1000 140 L992 150 L1000 160 L992 170 L1000 180 L976 180Z"/>
    <rect class="tone" x="22" y="0" width="956" height="180"/>
    <polygon class="panel" points="270,0 770,0 650,180 150,180"/>
    <rect class="badge" x="50" y="22" width="56" height="56" rx="8"/>
    <rect class="badge" x="50" y="100" width="56" height="56" rx="8"/>
    <circle class="ring" cx="310" cy="24" r="10"/>
    <circle class="dot" cx="380" cy="20" r="8"/>
    <circle class="ring" cx="460" cy="22" r="12"/>
    <circle class="ring" cx="610" cy="30" r="22"/>
    <circle class="dot" cx="640" cy="80" r="9"/>
    <circle class="ring" cx="560" cy="156" r="14"/>
    <circle class="dot" cx="615" cy="158" r="7"/>
    <circle class="ring" cx="200" cy="160" r="10"/>
    <text class="brand-name" x="240" y="112">Plume Crumb</text>
    <text class="benefits" x="745" y="70">+vitamin B12</text>
    <text class="benefits" x="760" y="100">biotin</text>
    <text class="benefits" x="760" y="130">collagen</text>
  </svg>

</main>
</body>
</html>
```